New modern and elegant label for Pisco La Cumbrera

Currently our supplier from Pisco La Cumbrera has a old-fashioned label. My distributors and clients have the opinion that the label blocks their sales, and I agree.
So I am looking for a modern, new label for these bottles. Basically I would let you be free in your design.
Pisco is a grape distillate, at about 40% alc. vol., origin is Peru.
La Cumbrera is a classic pisco producer, so that can be reflected in the label. The label itself doesnt have to be the same as it has been, otherwise shaped labels are fine too.
Attached, the current bottles (500ml and 700ml), also an image on how a clean 500ml bottle looks like.
Please surprise us, don't be shy in going in an a-typical way. Make your design shine!!!
Target Market(s)
Cocktail makers, end users, distrubutors, clients of liquor stores
Industry/Entity Type
Sales
Requirements
Must have
- A clean, modern look, whilst still connecting to the classicness of the brand La Cumbrera
Nice to have
- As an example of something different I put the Santa Brisa label idea. Modern, elegant and still classic. Not saying I want something like that literally, but could be used as a guideline on ideas

```html
<!DOCTYPE html>
<html lang="es">
<head>
<meta charset="utf-8">
<title>Pisco La Cumbrera – Label</title>
<link rel="stylesheet" href="https://fonts.googleapis.com/css2?family=Cormorant+Garamond:wght@500&family=Pinyon+Script&display=swap">
<style>
  :root {
    --paper: #ffffff;
    --ink: #1a1a1a;
    --ink-soft: #3a3a3a;
    --leaf-gold: #f2b630;
    --leaf-orange: #e5772a;
    --leaf-red: #d2452a;
    --bark: #5a5a5a;
  }
  * { margin: 0; padding: 0; box-sizing: border-box; }
  html, body {
    width: 800px;
    height: 1200px;
    overflow: hidden;
    background: var(--paper);
  }
  .label {
    position: relative;
    width: 800px;
    height: 1200px;
    color: var(--ink);
    font-family: "Cormorant Garamond", Georgia, serif;
  }
  .tree-illustration {
    position: absolute;
    left: 235px;
    top: 215px;
    width: 330px;
    height: 330px;
    border-radius: 46% 54% 30% 30% / 55% 50% 20% 20%;
    background:
      radial-gradient(circle at 30% 30%, var(--leaf-gold) 0 12%, transparent 40%),
      radial-gradient(circle at 70% 25%, var(--leaf-orange) 0 10%, transparent 38%),
      radial-gradient(circle at 55% 45%, var(--leaf-red) 0 6%, transparent 30%),
      linear-gradient(180deg, rgba(242,182,48,0.35) 0%, rgba(90,90,90,0.35) 75%, rgba(255,255,255,0) 100%);
    opacity: 0.85;
  }
  .brand-name {
    position: absolute;
    top: 578px;
    width: 100%;
    text-align: center;
    font-size: 58px;
    font-weight: 500;
    letter-spacing: 2px;
    line-height: 1;
  }
  .brand-rule {
    position: absolute;
    left: 60px;
    top: 655px;
    width: 680px;
    height: 5px;
    background: var(--ink);
  }
  .grape-variety {
    position: absolute;
    top: 685px;
    width: 100%;
    text-align: center;
    font-size: 40px;
    font-weight: 500;
    letter-spacing: 2px;
    line-height: 1;
    color: var(--ink-soft);
  }
  .product-type {
    position: absolute;
    top: 790px;
    width: 100%;
    text-align: center;
    font-family: "Pinyon Script", cursive;
    font-size: 130px;
    line-height: 1;
    color: var(--ink);
  }
  .legal-line {
    position: absolute;
    top: 1010px;
    width: 100%;
    text-align: center;
    font-size: 14px;
    letter-spacing: 1px;
    text-transform: uppercase;
    color: var(--ink-soft);
    white-space: nowrap;
  }
  .legal-line .sep { margin: 0 12px; }
</style>
</head>
<body>
  <main class="label">
    <div class="tree-illustration" role="img" aria-label="Ink illustration of an old gnarled tree with autumn leaves in gold, orange and red"></div>
    <h1 class="brand-name">LA CUMBRERA</h1>
    <div class="brand-rule"></div>
    <p class="grape-variety">PURO QUEBRANTA</p>
    <p class="product-type">Pisco</p>
    <p class="legal-line">
      Alc. 40% Vol.<span class="sep">|</span>Fundo San Isidro · Huarato · Palpa · Ica · Perú<span class="sep">|</span>500 ml
    </p>
  </main>
</body>
</html>
```